Postcard for our major fundraising event - LiftingDAWN2018

Bright Meadow YOUTH Camp (BMY) and Youth Summit Trail Camp (YSTC) are ministries of Larkwell Fellowship Church that serve Ventura County children of abuse, abandonment and neglect living in foster care. We are looking for a postcard design to promote our single largest fundraising event of the year, NurturingDAWN2018, to raise awareness and support for children of abuse. NurturingDAWN is a dinner banquet on at an exclusive outdoor venue, "Willow Hollow" with a rustic, ranch feel and with spectacular panoramic views of the City of Camarillo. The event will include music, refreshments, appetizers, a Santa Maria-style barbeque (BBQ), coffee and dessert, testimonials from camp, prize drawings, an opportunity to partner with BMY and YSTC, and time to socialize before and after.
Updates

I have just uploaded text copy to help designers come closer to what we are looking for. Thank you very much for your interest! -Dale

Target Market(s)

People from both within and from outside our sponsoring church who have a heart for hurting children and who are willing and able to financially support our camping (BMY & YSTC) ministries.

Industry/Entity Type

Church

Font styles to use
Serif
Decorative
Script

Requirements
Must have
• Name: NurturingDAWN2018... raising awareness and support for children of abuse
• Date: Thursday, May 24, 2018, 6:30-8:00 pm
• Place: Willow Hollow at Harlow Spread, 2715 Calder Lane, Somis, California.
• Cost: $30 per person
• Tickets: Available at Tixmoor.com
• Front side should include the elements of the event (although not necessarily bulleted like below):
• • Social hour
• • Music
• • Hors d’eourves
• • Refreshments
• • Santa Maria-style BBQ dinner
• • Coffee & dessert
• • Prize drawings
• • Stories from camp
• See attachment for suggested copy for back side.
• BMY and YSTC logos should be included on the postcard. I’ve uploaded a variety of photos for the designer to choose from; they do not necessarily all have to be included. There are also lots more pics available on our Pagebook (Bright Meadow YOUTH of Ventura).
• The front-side of the postcard can be entirely images and text. The back-side of the post card should include our return address at the top left ("BMY/YSTC of Larkwell Fellowship Church, 812 Fernbrook Court, Ventura, CA 93871") and should leave at least the right half of the postcard clear for addressing and postage.
• BMY colors are purple (Pantone 267) and red (Pantone 186). YSTC colors are green and yellow.
Nice to have
• A selection of camp photos large enough to easily view, but no so many that they are too small to identify. And, perhaps, a design element that evokes a rustic, outdoors, western, ranch feel, but not so much that it seems that we are promoting a country hoedown.
Should not have
• Anything sexual or sensual, related to alcoholic beverages, gambling, guns, or anything negative.

```html
<!DOCTYPE html>
<html lang="en">
<head>
<meta charset="utf-8">
<title>NurturingDAWN 2018 Postcard</title>
<link href="https://fonts.googleapis.com/css2?family=Montserrat:ital,wght@0,400;0,500;0,700;1,400;1,500&family=Dancing+Script:wght@500&display=swap" rel="stylesheet">
<style>
  :root {
    --purple: #3b2a78;
    --red: #d4202a;
    --white: #ffffff;
    --ink: #2a2a3a;
    --green: #2f9a3e;
    --yellow: #f1c22c;
    --stamp: #d6d6d6;
    --rule: #9a9aa6;
    --bg: #e9e9ec;
  }
  * { margin: 0; padding: 0; box-sizing: border-box; }
  html, body { width: 1200px; height: 903px; overflow: hidden; background: var(--bg); }
  body { position: relative; font-family: "Montserrat", sans-serif; color: var(--purple); }

  .postcard {
    position: absolute; width: 650px; height: 433px; background: var(--white);
    box-shadow: 0 8px 24px rgba(0,0,0,.22); overflow: hidden;
  }
  .postcard--front { left: 510px; top: 40px; }
  .postcard--back { left: 40px; top: 430px; }

  /* front */
  .front-art { position: absolute; inset: 0; }
  .activity { position: absolute; color: var(--white); font-size: 13px; font-weight: 500; letter-spacing: .3px; white-space: nowrap; }

  /* back */
  .brand-row { position: absolute; left: 22px; top: 16px; width: 300px; display: flex; align-items: center; justify-content: space-between; }
  .brand { display: flex; align-items: center; gap: 6px; font-weight: 700; font-size: 12px; color: var(--purple); }
  .brand__square { width: 10px; height: 10px; background: var(--red); }
  .brand__circle { width: 30px; height: 30px; border-radius: 50%; background: var(--green); border: 3px solid var(--yellow); }
  .brand--trail { color: var(--green); font-size: 10px; }
  .invite { position: absolute; left: 22px; top: 60px; width: 300px; font-size: 8.5px; line-height: 1.35; color: var(--ink); font-weight: 500; }
  .invite em { font-style: italic; }
  .title-band { position: absolute; left: 0; top: 100px; width: 338px; height: 34px; background: var(--red); display: flex; align-items: center; padding-left: 18px; }
  .title { color: var(--white); font-weight: 700; font-size: 21px; letter-spacing: .5px; }
  .tagline { position: absolute; left: 22px; top: 137px; font-family: "Dancing Script", cursive; font-size: 13px; color: var(--ink); }
  .venue { position: absolute; left: 22px; top: 160px; width: 300px; }
  .venue__lead { font-size: 10px; font-style: italic; color: var(--red); }
  .venue__name, .venue__addr { font-size: 13px; font-weight: 500; color: var(--purple); line-height: 1.3; }
  .date-row { position: absolute; left: 22px; top: 215px; display: flex; align-items: center; gap: 10px; }
  .date-pill { background: var(--red); color: var(--white); border-radius: 4px; padding: 2px 9px; font-size: 14px; font-weight: 500; }
  .time { font-size: 14px; font-weight: 500; color: var(--purple); }
  .tickets { position: absolute; left: 22px; top: 246px; display: flex; align-items: flex-end; gap: 12px; }
  .tickets__label { display: block; font-size: 9px; font-weight: 700; color: var(--red); margin-bottom: 2px; }
  .price { border: 1.5px solid var(--rule); border-radius: 4px; padding: 1px 8px; font-size: 17px; font-weight: 500; color: var(--purple); }
  .price strong { color: var(--red); font-weight: 700; }
  .availability { font-size: 11px; color: var(--ink); line-height: 1.2; }
  .availability a { color: var(--red); text-decoration: none; display: block; font-size: 12px; }
  .proceeds { position: absolute; left: 22px; top: 300px; width: 300px; font-size: 9px; line-height: 1.35; color: var(--ink); }
  .proceeds strong { color: var(--red); font-weight: 500; }
  .contact-panel { position: absolute; left: 0; top: 335px; width: 338px; height: 98px; background: var(--purple); color: var(--white); padding: 10px 18px; font-size: 8.5px; line-height: 1.4; }
  .contact-panel__heading { text-align: center; font-weight: 500; margin-bottom: 4px; }
  .contact-grid { display: flex; justify-content: space-between; }
  .contact__org { color: #ff7a80; font-weight: 700; }
  .contact__name { font-weight: 700; }

  .divider { position: absolute; left: 338px; top: 20px; width: 2px; height: 393px; background: var(--purple); }
  .return-address { position: absolute; left: 360px; top: 26px; font-size: 9px; line-height: 1.35; color: var(--ink); }
  .stamp-box { position: absolute; right: 28px; top: 30px; width: 62px; height: 62px; background: var(--stamp); }
  .address-line { position: absolute; left: 360px; width: 262px; height: 1px; background: var(--rule); }
</style>
</head>
<body>

<section class="postcard postcard--front" aria-label="Postcard front">
  <svg class="front-art" width="650" height="433" viewBox="0 0 650 433">
    <rect width="650" height="433" fill="#ffffff"/>
    <rect x="0" y="0" width="650" height="205" fill="#4a5a32" role="img" aria-label="Photo: campers riding horses on a shaded trail"/>
    <rect x="14" y="96" width="212" height="152" fill="#ffffff"/>
    <rect x="18" y="100" width="204" height="144" fill="#6f8a3c" role="img" aria-label="Photo: volunteers serving food at a camp banquet table"/>
    <rect x="226" y="122" width="212" height="146" fill="#ffffff"/>
    <rect x="230" y="126" width="204" height="138" fill="#c77a8c" role="img" aria-label="Photo: campers in pink sun hats at a party table"/>
    <rect x="438" y="146" width="212" height="136" fill="#ffffff"/>
    <rect x="442" y="150" width="208" height="128" fill="#5f8d3a" role="img" aria-label="Photo: a child practising archery with a counselor"/>
    <polygon points="0,248 650,290 650,415 0,415" fill="#ffffff"/>
    <polygon points="0,256 650,298 650,412 0,412" fill="var(--red)"/>
    <rect x="0" y="412" width="650" height="21" fill="var(--purple)"/>
  </svg>
  <span class="activity" style="left:34px;top:278px">Social hour</span>
  <span class="activity" style="left:22px;top:302px">Music</span>
  <span class="activity" style="left:156px;top:296px">Hors d’eourves</span>
  <span class="activity" style="left:144px;top:322px">Refreshments</span>
  <span class="activity" style="left:300px;top:326px">Santa Maria-style BBQ dinner</span>
  <span class="activity" style="left:290px;top:352px">Coffee &amp; dessert</span>
  <span class="activity" style="left:500px;top:352px">Prize drawings</span>
  <span class="activity" style="left:490px;top:378px">Stories from camp</span>
</section>

<section class="postcard postcard--back" aria-label="Postcard back">
  <div class="brand-row">
    <div class="brand"><span class="brand__square"></span>Bright Meadow YOUTH</div>
    <div class="brand brand--trail"><span class="brand__circle"></span>YSTC</div>
  </div>
  <p class="invite">Bright Meadow YOUTH Camp &amp; Youth Summit Trail Camp of Larkwell Fellowship Church <em>invite you to join us for</em></p>
  <div class="title-band"><h1 class="title">NurturingDAWN 2018</h1></div>
  <p class="tagline">raising awareness and support for children of abuse</p>
  <div class="venue">
    <p class="venue__lead">at the exclusive</p>
    <p class="venue__name">Willow Hollow at Harlow Spread</p>
    <p class="venue__addr">2715 Calder Lane, Somis, CA</p>
  </div>
  <div class="date-row">
    <span class="date-pill">Thursday, May 24, 2018</span>
    <span class="time">6:30-8:00 pm</span>
  </div>
  <div class="tickets">
    <div>
      <span class="tickets__label">TICKETS:</span>
      <span class="price"><strong>$30</strong> per person</span>
    </div>
    <p class="availability">Available at <a href="#">Tixmoor.com</a></p>
  </div>
  <p class="proceeds">All proceeds to benefit <strong>BMY &amp; YSTC serving children of abuse ages 7-14.</strong></p>
  <div class="contact-panel">
    <p class="contact-panel__heading">For more information:</p>
    <div class="contact-grid">
      <div class="contact">
        <p class="contact__org">BMY:</p>
        <p class="contact__name">Dale Brennick (Director)</p>
        <p>&#9742; (805) 555-0142</p>
        <p>&#9993; bmyventura@mailhub.net</p>
      </div>
      <div class="contact">
        <p class="contact__org">YSTC:</p>
        <p class="contact__name">Noel Varga (Director)</p>
        <p>&#9742; (805) 555-0187</p>
        <p>&#9993; noelvargaphoto@postmail.com</p>
      </div>
    </div>
  </div>

  <div class="divider"></div>
  <address class="return-address" style="font-style:normal">
    BMY/YSTC of<br>Larkwell Fellowship Church,<br>812 Fernbrook Court,<br>Ventura, CA 93871
  </address>
  <div class="stamp-box"></div>
  <div class="address-line" style="top:230px"></div>
  <div class="address-line" style="top:272px"></div>
  <div class="address-line" style="top:314px"></div>
</section>

</body>
</html>
```